Investment company needing business card

We are wanting a business card which looks sharp and easy on the eye. We are thinking of having a business card with the logo embossed on it, to really make it stand out. We will only have a small amount of information of the business card, person's name, position, email address and phone number

Contact Information for Business Card

Danica Pruett
Executive Assistant
+64 21 547 3162
danicap@harwellcapital.co.nz

Requirements
Must have
• Embossed logo
Should not have
• Not to be busy

```html
<!DOCTYPE html>
<html lang="en">
<head>
<meta charset="utf-8">
<title>Harwell Capital – Business Card</title>
<link rel="stylesheet" href="https://fonts.googleapis.com/css2?family=Montserrat:wght@400;700&display=swap">
<style>
  :root {
    --backdrop: #e6e5eb;
    --card-grey: #5f5f61;
    --card-white: #ffffff;
    --green-light: #22b573;
    --green-dark: #1a6c47;
    --text-light: #ffffff;
    --text-muted: #d9d9d9;
    --emboss: rgba(255,255,255,0.07);
  }
  * { margin: 0; padding: 0; box-sizing: border-box; }
  html, body {
    width: 1200px; height: 1200px; overflow: hidden;
    background: var(--backdrop);
    font-family: "Montserrat", Arial, sans-serif;
  }
  .card {
    position: absolute; left: 100px; top: 314px;
    width: 1000px; height: 572px;
    overflow: hidden;
    box-shadow: 0 18px 40px rgba(0,0,0,0.18);
  }
  .card-shapes { position: absolute; inset: 0; }
  .emboss-mark {
    position: absolute; left: 830px; top: 300px;
    width: 140px; height: 140px;
    background: var(--emboss);
    border-radius: 14px;
  }
  .brand {
    position: absolute; left: 60px; top: 292px; width: 340px;
    text-align: center;
    color: var(--green-light);
    font-weight: 700; font-size: 40px; line-height: 1.15; letter-spacing: 1px;
  }
  .contact {
    position: absolute; right: 60px; top: 70px; text-align: right;
    color: var(--text-light);
  }
  .contact-name {
    font-weight: 700; font-size: 46px; letter-spacing: 1px; line-height: 1;
    margin-right: 58px;
  }
  .contact-title {
    font-weight: 400; font-size: 15px; letter-spacing: 5px;
    color: var(--text-muted); margin-top: 8px; margin-right: 58px;
  }
  .contact-line {
    display: flex; align-items: center; justify-content: flex-end; gap: 16px;
    font-size: 19px; font-weight: 400; letter-spacing: 1px;
    margin-top: 18px;
  }
  .contact-line.email { margin-top: 36px; }
  .contact-icon {
    width: 40px; height: 40px; border-radius: 50%;
    background: var(--card-white);
    display: flex; align-items: center; justify-content: center;
  }
  .contact-icon svg { width: 22px; height: 22px; }
</style>
</head>
<body>
  <div class="card">
    <svg class="card-shapes" viewBox="0 0 1000 572" width="1000" height="572" aria-hidden="true">
      <rect width="1000" height="572" fill="var(--card-grey)"/>
      <path d="M395 175 C520 300 620 470 820 572 L455 572 Z" fill="var(--green-light)"/>
      <path d="M395 175 C470 300 520 440 560 572 L455 572 Z" fill="var(--green-dark)"/>
      <path d="M0 0 L60 0 C300 30 420 140 455 290 C480 400 475 490 455 572 L0 572 Z" fill="var(--card-white)"/>
    </svg>

    <div class="emboss-mark"></div>

    <div class="brand">HARWELL<br>CAPITAL</div>

    <div class="contact">
      <div class="contact-name">DANICA PRUETT</div>
      <div class="contact-title">EXECUTIVE ASSISTANT</div>
      <div class="contact-line phone">
        <span>+64 21 547 3162</span>
        <span class="contact-icon">
          <svg viewBox="0 0 24 24"><path fill="#22b573" d="M6.6 10.8a15 15 0 0 0 6.6 6.6l2.2-2.2a1 1 0 0 1 1-.25 11.4 11.4 0 0 0 3.6.57 1 1 0 0 1 1 1V20a1 1 0 0 1-1 1A17 17 0 0 1 3 4a1 1 0 0 1 1-1h3.5a1 1 0 0 1 1 1c0 1.250.2 2.450.57 3.57a1 1 0 0 1-.25 1z"/></svg>
        </span>
      </div>
      <div class="contact-line email">
        <span>danicap@harwellcapital.co.nz</span>
        <span class="contact-icon">
          <svg viewBox="0 0 24 24"><rect x="3" y="6" width="18" height="12" rx="1.5" fill="#22b573"/><path d="M3.5 6.8 12 13l8.5-6.2" fill="none" stroke="#fff" stroke-width="1.6"/></svg>
        </span>
      </div>
    </div>
  </div>
</body>
</html>
```